Plate Bright Workshop (workshop to teach people to eat fruits and vegetables)

Double sided DL Flyer

Free Community Workshop
Plate Bright Live Lively
Central Coast NSW

Copy to appear on flyer side one:-
PLATE BRIGHT LIVE LIVELY
interactive workshops
March-April 2019
Presented by qualified nutritionist

Food for healthier happier life for you and your family (free to central coast residents - all ages welcome

Side 2
Learn About:-
Foods that improve your health
basic nutrition
gut brain connection
portion size
menu planning
preparation
eating

Benefits
Improved health
Improved Energy
Manage chronic illness
diabetes type II
cholesterol
Blood Pressure
Family fun

Food Tastings
Lucky Door Prize

Reserve for spot online @ www.platebright.com.au or call 0462 508 731
Supported by Harbourline Shire Council (Logo) Harbourline Rugby Social Club (Logo) Pindara Veterans Club (Logo)

I would like to see a flyer that is bright, fun and fresh with images of fresh food.

Target Market(s)

Women 30 plus

Industry/Entity Type

Health And Wellness

Logo Text

PLATE BRIGHT LIVE LIVELY

Font styles to use
Other font styles liked:
• bold clean

Colors
f37122
9bcb3c
fbed22
ec1f27
e34297

Requirements
Must have
• bright eye catching colours featuring fresh fruit and vegetables
• I have attached a some images of designs I like
Nice to have
• Im happy for the designer to change copy to create a clean flyer without loosing essential information
• I like the feel of the banner on my facebook page
• Kindly Nourish - Plate Bright Live Lively with Megan Troute
• https://www.facebook.com/kindlynourishoz/
Should not have
• old fashioned images

```html
<!DOCTYPE html>
<html lang="en">
<head>
<meta charset="utf-8">
<title>Plate Bright Live Lively – DL Flyer</title>
<link rel="stylesheet" href="https://fonts.googleapis.com/css2?family=Bebas+Neue&family=Roboto+Condensed:wght@700&family=Lato:wght@400;700&display=swap">
<style>
  :root {
    --page-bg: #e4e1dc;
    --panel-dark: #3a3939;
    --panel-orange: #e27633;
    --accent-blue: #1ab2e8;
    --white: #ffffff;
    --ink: #1d1d1d;
    --wood-dark: #4a3129;
    --wood-mid: #6b4a3e;
    --leaf: #3f7a2c;
    --tomato: #d8322a;
    --pepper: #f2c31c;
  }
  * { box-sizing: border-box; margin: 0; padding: 0; }
  html, body { width: 1200px; height: 1200px; overflow: hidden; }
  body { background: var(--page-bg); position: relative; font-family: "Lato", sans-serif; }

  .flyer {
    position: absolute; left: 114px; width: 972px; height: 459px;
    overflow: hidden; box-shadow: 0 4px 6px rgba(0,0,0,0.25);
  }
  .flyer--front { top: 84px; }
  .flyer--back { top: 626px; }

  .photo { position: absolute; top: 0; height: 100%; }
  .photo--front-main {
    left: 0; width: 461px;
    background:
      radial-gradient(circle at 45% 55%, rgba(242,195,28,0.55) 0 18%, transparent 40%),
      radial-gradient(circle at 55% 35%, rgba(216,50,42,0.55) 0 15%, transparent 35%),
      radial-gradient(circle at 20% 40%, rgba(63,122,44,0.8) 0 20%, transparent 45%),
      linear-gradient(90deg, var(--wood-dark), var(--wood-mid) 50%, var(--wood-dark));
  }
  .photo--back-main {
    left: 0; width: 371px;
    background:
      radial-gradient(circle at 20% 30%, rgba(63,122,44,0.85) 0 22%, transparent 45%),
      radial-gradient(circle at 15% 80%, rgba(216,50,42,0.55) 0 12%, transparent 35%),
      radial-gradient(circle at 45% 15%, rgba(63,122,44,0.7) 0 12%, transparent 30%),
      linear-gradient(90deg, var(--wood-dark), var(--wood-mid) 60%, var(--wood-dark));
  }
  .photo--edge {
    right: 0; width: 24px;
    background: linear-gradient(180deg, var(--tomato), var(--leaf) 30%, var(--leaf) 70%, var(--tomato));
  }

  .panel { position: absolute; top: 0; height: 100%; }
  .panel--dark { left: 461px; width: 488px; background: var(--panel-dark); text-align: center; color: var(--white); }
  .panel--orange { left: 371px; width: 578px; background: var(--panel-orange); color: var(--white); }

  .headline {
    position: absolute; left: 0; right: 0; top: 44px;
    font-family: "Bebas Neue", sans-serif; font-size: 102px; line-height: 98px; letter-spacing: 0;
  }
  .date-box {
    position: absolute; left: 66px; top: 262px; width: 350px; height: 85px;
    background: var(--accent-blue); font-family: "Roboto Condensed", sans-serif; font-weight: 700;
    padding-top: 4px;
  }
  .date-box__dates { font-size: 38px; line-height: 44px; }
  .date-box__place { font-size: 28px; line-height: 34px; }
  .details { position: absolute; left: 0; right: 0; top: 359px; font-size: 13px; line-height: 16px; }
  .details__presenter { margin-top: 7px; }

  .column { position: absolute; top: 36px; }
  .column--learn { left: 14px; }
  .column--benefits { left: 336px; }
  .column__title { font-family: "Roboto Condensed", sans-serif; font-weight: 700; font-size: 35px; line-height: 42px; margin-bottom: 8px; }
  .checklist { list-style: none; }
  .checklist li { display: flex; align-items: center; font-size: 18.5px; line-height: 32.6px; white-space: nowrap; }
  .checklist svg { width: 19px; height: 19px; margin-right: 9px; flex: none; }

  .reserve {
    position: absolute; left: 39px; top: 334px; width: 488px; height: 88px;
    background: var(--white); color: var(--ink); text-align: center;
    font-weight: 700; font-size: 19px; line-height: 23.5px; padding-top: 8px;
  }
</style>
</head>
<body>
<svg width="0" height="0" style="position:absolute">
  <defs>
    <symbol id="tick" viewBox="0 0 20 20">
      <circle cx="10" cy="10" r="10" fill="#ffffff"/>
      <path d="M5.5 10.3l3 3 6-6.3" fill="none" stroke="#e27633" stroke-width="2.4" stroke-linecap="round" stroke-linejoin="round"/>
    </symbol>
  </defs>
</svg>

<section class="flyer flyer--front">
  <div class="photo photo--front-main" role="img" aria-label="Fresh fruit and vegetables on a wooden table forming a waist silhouette wrapped with a measuring tape"></div>
  <div class="panel panel--dark">
    <h1 class="headline">PLATE BRIGHT<br>LIVE LIVELY</h1>
    <div class="date-box">
      <div class="date-box__dates">March &amp; April 2019</div>
      <div class="date-box__place">Central Coast</div>
    </div>
    <div class="details">
      <p>Food for a&nbsp; Healthir happier Life for you and your family</p>
      <p>Free for NSW Central coast residents</p>
      <p>All ages welcome</p>
      <p class="details__presenter">Presented by qualified Nutritionist</p>
    </div>
  </div>
  <div class="photo photo--edge" role="img" aria-label="Strip of fresh greens and tomatoes"></div>
</section>

<section class="flyer flyer--back">
  <div class="photo photo--back-main" role="img" aria-label="Brussels sprouts, cherry tomatoes, rocket, lime and chilli on a wooden table"></div>
  <div class="panel panel--orange">
    <div class="column column--learn">
      <h2 class="column__title">Learn About:</h2>
      <ul class="checklist">
        <li><svg><use href="#tick"/></svg>Foods that improve your health</li>
        <li><svg><use href="#tick"/></svg>Basic nutrition</li>
        <li><svg><use href="#tick"/></svg>Gut brain connection</li>
        <li><svg><use href="#tick"/></svg>Portion size</li>
        <li><svg><use href="#tick"/></svg>Menu planning</li>
        <li><svg><use href="#tick"/></svg>Preparation</li>
        <li><svg><use href="#tick"/></svg>Eating</li>
      </ul>
    </div>
    <div class="column column--benefits">
      <h2 class="column__title">Benefits:</h2>
      <ul class="checklist">
        <li><svg><use href="#tick"/></svg>Improved Health</li>
        <li><svg><use href="#tick"/></svg>Improved Energy</li>
        <li><svg><use href="#tick"/></svg>Manage Chronic Illness</li>
        <li><svg><use href="#tick"/></svg>Diabetes Type II</li>
        <li><svg><use href="#tick"/></svg>Cholesterol</li>
        <li><svg><use href="#tick"/></svg>Blood Pressure</li>
        <li><svg><use href="#tick"/></svg>Family fun</li>
      </ul>
    </div>
    <div class="reserve">
      <p>Reserve your spot online at</p>
      <p>www.platebright.com.au</p>
      <p>call 0462 508 731</p>
    </div>
  </div>
  <div class="photo photo--edge" role="img" aria-label="Strip of fresh greens and tomatoes"></div>
</section>
</body>
</html>
```